Zielgruppe
Planung und Realisierung von individuellen und wertbeständigen Kamin- und Ofenlösungen, sowie Fliesen- und Baddesign.
Aufgabenstellung
Wir benötigen ein möglichst schlichtes Design für Visitenkarten, bzw. Briefpapier. Für die Visitenkarten gerne auch Vorschläge mit Prägung, Ausstanzung oder mit Heißfolie. Auch Klappkarten wären denkbar. Das Design soll "das gewisse Etwas haben" und nicht zu verspielt sein.
Die Visitenkarten sind für die Firma KARMU, das Logo von der Ausstellung "talgrund" soll dezent mit eingebunden werden (bei dem Briefpapier z.B. in der Fußzeile". Die farbliche Gestaltung sollte sich an den Farben des Logos orientieren.
Schriftart für Texte: Century Gothic
Schriftfarbe: RAL 7016
Nur eine Idee: Ich könnte mir auch gut vorstellen, dass die Visitenkarte aus einer Zündholzverpackung (wenn dann aber eine besondere mit nur einem Zündholz oder einem besonders breiten) besteht: http://lindoraversand.de/produkte_briefchen.php

```html
<!DOCTYPE html>
<html lang="de">
<head>
<meta charset="utf-8">
<title>KARMU Visitenkarte</title>
<link href="https://fonts.googleapis.com/css2?family=Questrial&display=swap" rel="stylesheet">
<style>
  :root {
    --backdrop: #c09a5e;
    --paper: #ffffff;
    --ink: #293133;
    --logo-ink: #000000;
    --night: #162426;
    --flame: #ff7300;
    --muted: #8a8f90;
  }
  * { margin: 0; padding: 0; box-sizing: border-box; }
  html, body { width: 1200px; height: 1120px; overflow: hidden; }
  body {
    background: var(--backdrop);
    font-family: "Questrial", "Century Gothic", sans-serif;
    color: var(--ink);
    position: relative;
  }
  .card {
    position: absolute;
    left: 271px;
    width: 603px;
    height: 390px;
  }
  .card--front { top: 112px; background: var(--paper); }
  .card--back { top: 571px; background: var(--night); }

  .card > * { position: absolute; white-space: nowrap; }

  .brand-name {
    left: 24px; top: 14px;
    font-size: 68px;
    line-height: 1;
    letter-spacing: 2px;
    color: var(--logo-ink);
  }
  .brand-tagline {
    left: 25px; top: 76px;
    font-size: 19px;
    color: var(--logo-ink);
  }
  .holder-name {
    right: 25px; top: 185px;
    font-size: 36px;
    line-height: 1;
  }
  .holder-role {
    right: 25px; top: 224px;
    font-size: 14px;
  }
  .address {
    left: 25px; top: 253px;
    font-size: 20px;
    line-height: 24px;
    letter-spacing: 1.6px;
    font-style: normal;
  }
  .address .gap { display: inline-block; width: 24px; }
  .phone {
    left: 25px; top: 308px;
    font-size: 17px;
    line-height: 21px;
  }
  .phone .label { display: inline-block; width: 49px; }
  .email, .web {
    top: 357px;
    font-size: 15px;
    letter-spacing: 1.6px;
  }
  .email { left: 24px; }
  .web { right: 20px; }

  .back-mark {
    left: 0; right: 0; top: 148px;
    text-align: center;
    font-size: 92px;
    line-height: 1;
    letter-spacing: 4px;
    color: var(--flame);
  }
  .partner-name {
    right: 17px; top: 348px;
    font-size: 21px;
    color: var(--muted);
  }
</style>
</head>
<body>
  <section class="card card--front" aria-label="Vorderseite">
    <div class="brand-name">KARMU</div>
    <div class="brand-tagline">kamine · öfen · fliesen</div>
    <div class="holder-name">Lukas Karmu</div>
    <div class="holder-role">Geschäftsführer</div>
    <address class="address">Am Lindenhang 12<br>34512<span class="gap"></span>Talheim</address>
    <div class="phone"><span class="label">fon:</span>05627 / 41 73 50<br><span class="label">fax:</span>05627 / 41 73 58</div>
    <div class="email">info@karmu-talheim.de</div>
    <div class="web">www.karmu-talheim.de</div>
  </section>

  <section class="card card--back" aria-label="Rückseite">
    <div class="back-mark">KARMU</div>
    <div class="partner-name">talgrund</div>
  </section>
</body>
</html>
```